Business Card Design Project - 2 sided

We need a business card design for a card having one business on each side (ie. two businesses on one card). Would like a design that incorporates logo, tagline and normal fields (name, position, address, phone).

Would also like an allowance for small font text along the bottom (text to be determined, but less than 50 characters).

NB. Attached logo for Verbal Bridgeworks has two variations - either can be used.

www.verbalbridgeworks.com / www.kelpora.com

```html
<!DOCTYPE html>
<html lang="en">
<head>
<meta charset="utf-8">
<title>Two-sided business card – Verbal Bridgeworks / Kelpora</title>
<link rel="stylesheet" href="https://fonts.googleapis.com/css2?family=Open+Sans:wght@400;600;700&display=swap">
<style>
  :root {
    --page: #eef0f2;
    --card: #ffffff;
    --green: #8cc63f;
    --green-light: #a3d35a;
    --navy: #1f2177;
    --blue: #2684bd;
    --blue-light: #3cb4e6;
    --white: #ffffff;
    --ink-soft: rgba(255,255,255,0.85);
  }
  * { box-sizing: border-box; margin: 0; padding: 0; }
  html, body {
    width: 1200px; height: 900px; overflow: hidden;
    background: var(--page);
    font-family: "Open Sans", Arial, sans-serif;
  }
  .sheet {
    position: relative; width: 1200px; height: 900px;
    display: flex; flex-direction: column; align-items: center; justify-content: center; gap: 40px;
  }
  .card {
    position: relative; width: 680px; height: 390px;
    background: var(--card); border-radius: 22px; overflow: hidden;
    box-shadow: 0 6px 18px rgba(0,0,0,0.12);
  }
  .card__panel { position: absolute; inset: 0; width: 680px; height: 390px; }

  .brand { position: absolute; left: 40px; top: 28px; display: flex; align-items: center; gap: 12px; }
  .brand__name { font-weight: 700; font-size: 32px; color: var(--navy); letter-spacing: -0.3px; line-height: 1; }
  .brand__dot { width: 44px; height: 44px; border-radius: 50%; background: var(--green); }

  .tagline {
    position: absolute; right: 44px; top: 112px; text-align: right;
    color: var(--green); font-size: 17px; line-height: 1.3;
  }

  .contact { position: absolute; left: 40px; top: 118px; color: var(--white); }
  .contact__name { font-weight: 700; font-size: 30px; line-height: 1.1; }
  .contact__role { font-size: 13px; color: var(--ink-soft); margin-top: 2px; }
  .contact__address { font-weight: 600; font-size: 13px; margin-top: 22px; }
  .contact__line { display: flex; align-items: center; gap: 8px; font-size: 13px; margin-top: 6px; }
  .contact__line:first-of-type { margin-top: 10px; }
  .icon { width: 13px; height: 13px; flex: none; }

  .website {
    position: absolute; left: 40px; bottom: 44px;
    display: flex; align-items: center; gap: 8px;
    font-weight: 700; font-size: 15px;
  }
  .card--bridgeworks .website { color: var(--navy); }
  .card--kelpora .website { color: var(--green); }
</style>
</head>
<body>
<main class="sheet">

  <!-- Side one: Verbal Bridgeworks -->
  <section class="card card--bridgeworks">
    <svg class="card__panel" viewBox="0 0 680 390" aria-hidden="true">
      <path d="M0 100 H300 L460 292 H240 L222 312 L204 292 H0 Z" fill="var(--green)"/>
    </svg>

    <div class="brand"><span class="brand__name">Verbal Bridgeworks</span></div>
    <p class="tagline">Website Translation and<br>Localisation Specialists…</p>

    <div class="contact">
      <p class="contact__name">Miriam Delacroix</p>
      <p class="contact__role">Business Development</p>
      <p class="contact__address">42 Linden Road, Kew VIC 3101, AUSTRALIA</p>
      <p class="contact__line">
        <svg class="icon" viewBox="0 0 16 16"><path d="M4 1 L6.5 4.5 L5 6.5 C6 8.5 7.5 10 9.5 11 L11.5 9.5 L15 12 L13 15 C7 14.5 1.5 9 1 3 Z" fill="currentColor"/></svg>
        +61 3 9000 4172 (Australia)
      </p>
      <p class="contact__line">
        <svg class="icon" viewBox="0 0 16 16"><rect x="1" y="3" width="14" height="10" rx="1.5" fill="none" stroke="currentColor" stroke-width="1.6"/><path d="M1.5 4 L8 9 L14.5 4" fill="none" stroke="currentColor" stroke-width="1.6"/></svg>
        info@verbalbridgeworks.com
      </p>
    </div>

    <p class="website">
      <svg class="icon" viewBox="0 0 16 16"><circle cx="8" cy="8" r="6.5" fill="none" stroke="currentColor" stroke-width="1.6"/><path d="M1.5 8 H14.5 M8 1.5 C5 5 5 11 8 14.5 M8 1.5 C11 5 11 11 8 14.5" fill="none" stroke="currentColor" stroke-width="1.2"/></svg>
      http://www.verbalbridgeworks.com/
    </p>
  </section>

  <!-- Side two: Kelpora -->
  <section class="card card--kelpora">
    <svg class="card__panel" viewBox="0 0 680 390" aria-hidden="true">
      <defs>
        <linearGradient id="kelpora-panel" x1="0" y1="0" x2="1" y2="1">
          <stop offset="0" stop-color="var(--blue)"/>
          <stop offset="1" stop-color="var(--blue-light)"/>
        </linearGradient>
      </defs>
      <path d="M0 100 H430 L520 292 H300 L282 312 L264 292 H0 Z" fill="url(#kelpora-panel)"/>
    </svg>

    <div class="brand">
      <span class="brand__dot"></span>
      <span class="brand__name">Kelpora LLC</span>
    </div>

    <div class="contact">
      <p class="contact__name">Miriam Delacroix</p>
      <p class="contact__role">Business Development</p>
      <p class="contact__address">Marlowe Drive, Port Sable, Florida, 34600, USA</p>
      <p class="contact__line">
        <svg class="icon" viewBox="0 0 16 16"><path d="M4 1 L6.5 4.5 L5 6.5 C6 8.5 7.5 10 9.5 11 L11.5 9.5 L15 12 L13 15 C7 14.5 1.5 9 1 3 Z" fill="currentColor"/></svg>
        +1 314-555-0186
      </p>
      <p class="contact__line">
        <svg class="icon" viewBox="0 0 16 16"><rect x="1" y="3" width="14" height="10" rx="1.5" fill="none" stroke="currentColor" stroke-width="1.6"/><path d="M1.5 4 L8 9 L14.5 4" fill="none" stroke="currentColor" stroke-width="1.6"/></svg>
        support@kelpora.com
      </p>
    </div>

    <p class="website">
      <svg class="icon" viewBox="0 0 16 16"><circle cx="8" cy="8" r="6.5" fill="none" stroke="currentColor" stroke-width="1.6"/><path d="M1.5 8 H14.5 M8 1.5 C5 5 5 11 8 14.5 M8 1.5 C11 5 11 11 8 14.5" fill="none" stroke="currentColor" stroke-width="1.2"/></svg>
      http://www.kelpora.com/
    </p>
  </section>

</main>
</body>
</html>
```